Divorce marketing brochure - Which will include a toy ball and chain as a gimick

A single page marketing enclosure which includes a toy ball and chain to be given to lawyers. I want to convey the following messages:

1. We pay a 1/3 referral fee;
2. We solve difficult problems.

Examples of problems solved:
*Litigation of complex property, custody, support and parenting time issues;
*Protection (or invasion) of personal injury proceeds in divorce;
*Distribution of consortium proceeds in divorce;
*Pre-nuptial and Post-nuptial agreements.
*Settlements
*Reduce conflict

A sample of the toy ball and chain enclosure can be viewed here:

My website is www.thesplitcounsel.com (currently being updated - who's isn't?)

http://www.shopvexto.com/Orbel-Trinkets-Inc-Convict-Shackle/dp/K7QX3MZP21/ref=sr_1_9?ie=UTF8&qid=1311011554&sr=8-9

Target Market(s)

Personal Injury Attorneys

Industry/Entity Type

Marketing

Requirements
Must have
• Call to action:

www.thesplitcounsel.com
1-877-HIRE-TEAM
248-555-7182
Marcus@brevanlegal.com
Nice to have
• I want this campaign to stand out. Different is good. I am a divorce lawyer marketing to personal injury attorneys (and some others) for divorce referrals. (No one forgets the girl with red hair and braces) I want the campaign to be remembered without being offensive.
Should not have

```html
<!DOCTYPE html>
<html lang="en">
<head>
<meta charset="utf-8">
<title>Choosing the right divorce attorney</title>
<link rel="stylesheet" href="https://fonts.googleapis.com/css2?family=Source+Sans+3:wght@400;600;700;800&display=swap">
<style>
  :root {
    --navy: #1b3c7c;
    --navy-deep: #173570;
    --header-grey: #d6d6d8;
    --fade-blue: #6a7fb0;
    --paper: #ffffff;
    --ink: #1e3a78;
    --steel-light: #f2f2f3;
    --steel-dark: #8d8f94;
  }
  * { margin: 0; padding: 0; box-sizing: border-box; }
  html, body { width: 849px; height: 1200px; overflow: hidden; }
  body {
    font-family: "Source Sans 3", "Myriad Pro", Arial, sans-serif;
    background: var(--paper);
  }
  .flyer {
    position: relative;
    width: 849px;
    height: 1200px;
    overflow: hidden;
    background: linear-gradient(90deg, var(--paper) 0%, #eef0f6 35%, #a9b5d2 70%, var(--fade-blue) 100%);
  }
  .flyer::after {
    content: "";
    position: absolute;
    left: 0; right: 0; top: 760px; bottom: 0;
    background: linear-gradient(180deg, rgba(255,255,255,0) 0%, var(--paper) 60%);
    pointer-events: none;
    z-index: 0;
  }
  .masthead {
    position: absolute;
    left: 71px; top: 0;
    width: 778px; height: 217px;
    background: var(--header-grey);
    z-index: 1;
  }
  .masthead__kicker {
    position: absolute;
    left: 31px; top: 76px;
    font-size: 47px; font-weight: 700;
    color: var(--paper);
    line-height: 1;
  }
  .masthead__title {
    position: absolute;
    left: 29px; top: 130px;
    font-size: 72px; font-weight: 800;
    color: var(--navy);
    line-height: 1;
    letter-spacing: -0.5px;
  }
  .ball-and-chain {
    position: absolute;
    left: 0; top: 300px;
    width: 300px; height: 900px;
    background: radial-gradient(ellipse at 40% 20%, var(--steel-light) 0%, #c4c5c9 30%, rgba(160,162,167,0.35) 60%, rgba(255,255,255,0) 85%);
    z-index: 1;
  }
  .intro {
    position: absolute;
    left: 217px; top: 318px;
    width: 560px;
    z-index: 2;
  }
  .intro__question {
    font-size: 28px; font-weight: 700;
    color: var(--navy);
    line-height: 1.1;
  }
  .intro__body {
    margin: 12px 0 0 50px;
    font-size: 20.5px;
    line-height: 26px;
    color: var(--ink);
  }
  .badge {
    position: absolute;
    border-radius: 50%;
    background: var(--navy);
    color: var(--paper);
    font-weight: 700;
    display: flex;
    align-items: center;
    justify-content: center;
    text-align: center;
    z-index: 3;
  }
  .badge--referral {
    left: 600px; top: 540px;
    width: 224px; height: 224px;
    font-size: 31px; line-height: 1.08;
    box-shadow: 4px 4px 0 rgba(255,255,255,0.6);
  }
  .badge--problems {
    left: 68px; top: 787px;
    width: 196px; height: 196px;
    font-size: 30px; line-height: 1.1;
  }
  .services {
    position: absolute;
    left: 356px; top: 744px;
    width: 493px; height: 397px;
    background: var(--navy-deep);
    color: var(--paper);
    padding: 20px 0 0 16px;
    z-index: 2;
  }
  .services__title {
    font-size: 27px; font-weight: 700;
    margin-bottom: 12px;
  }
  .services__list {
    list-style: none;
    font-size: 19.5px;
    line-height: 26px;
  }
  .services__list li {
    padding-left: 12px;
    text-indent: -12px;
  }
  .services__list li::before { content: "\2022\00a0"; }
  .services__list .indent-1 { padding-left: 80px; }
  .services__list .indent-2 { padding-left: 112px; }
  .contact {
    position: absolute;
    left: 71px; top: 1073px;
    color: var(--ink);
    z-index: 4;
  }
  .contact__cta {
    font-size: 26px; font-weight: 700;
    color: var(--navy);
    margin-bottom: 8px;
  }
  .contact__line {
    font-size: 17px;
    line-height: 29px;
  }
  .website {
    position: absolute;
    left: 533px; top: 1148px;
    font-size: 21px; font-weight: 700;
    color: var(--navy);
    z-index: 4;
  }
</style>
</head>
<body>
  <main class="flyer">
    <header class="masthead">
      <p class="masthead__kicker">Choosing the right</p>
      <h1 class="masthead__title">divorce attorney</h1>
    </header>

    <div class="ball-and-chain" role="img" aria-label="Chrome ball and chain with an open shackle cuff"></div>

    <section class="intro">
      <h2 class="intro__question">Are you planning a divorce?</h2>
      <p class="intro__body">Divorce is stressful for most, for some it is a relief. A person will usually experience some form of denial, shock and confusion before being able to let go of the relationship. Unfortunately, in addition to navigating the emotional component of a divorce, you must also choose an attorney.</p>
    </section>

    <div class="badge badge--referral"><span>We pay<br>a 1/3<br>referral fee;</span></div>

    <section class="services">
      <h2 class="services__title">We deal with...</h2>
      <ul class="services__list">
        <li>Litigation of complex property, custody, support and parenting time issues;</li>
        <li>Protection (or invasion) of personal injury proceeds in divorce;</li>
        <li>Distribution of consortium proceeds in divorce;</li>
        <li>Pre-nuptial and Post-nuptial agreements.</li>
        <li class="indent-1">Settlements</li>
        <li class="indent-2">Reduce conflict</li>
      </ul>
    </section>

    <div class="badge badge--problems"><span>We solve<br>difficult<br>problems.</span></div>

    <footer class="contact">
      <p class="contact__cta">Call now</p>
      <p class="contact__line">1-877-HIRE-TEAM</p>
      <p class="contact__line">t : 248-555-7182 - Marcus@brevanlegal.com</p>
    </footer>
    <p class="website">www.thesplitcounsel.com</p>
  </main>
</body>
</html>
```